Diesel Fitting/Mechanical Company Needs a new Business Card

We would like a new business card that showcases our logo and business information.

Industry/Entity Type

Business

Contact Information for Business Card

314 Wendale Street
PO Box 7581 CHARTERS TOWERS QLD 4820
Phone: 49312787 Fax: 49312688 Mobile: 0438915276 ABN: 63 519 087 342

Requirements
Must have
• The following email addresses:
• admin@tkservicing.com.au , sales@tkservicing.com.au , accounts@tkservicing.com.au , parts@tkservicing.com.au , office@tkservicing.com.au
• Also need to have the website: www.tkservicing.com.au

```html
<!DOCTYPE html>
<html lang="en">
<head>
<meta charset="UTF-8">
<title>TK Servicing – Business Card Back</title>
<link href="https://fonts.googleapis.com/css2?family=Nunito+Sans:wght@300;800&display=swap" rel="stylesheet">
<style>
  :root {
    --backdrop: #240d12;
    --card-yellow: #ffc107;
    --ink: #000000;
  }
  html, body {
    margin: 0;
    padding: 0;
    width: 1200px;
    height: 1200px;
    overflow: hidden;
    background: var(--backdrop);
  }
  .canvas {
    position: relative;
    width: 1200px;
    height: 1200px;
    background: var(--backdrop);
    font-family: "Nunito Sans", "Avenir Next", sans-serif;
    color: var(--ink);
  }
  .card {
    position: absolute;
    left: 50px;
    top: 255px;
    width: 1101px;
    height: 629px;
    background: var(--card-yellow);
  }
  .contact {
    position: absolute;
    left: 300px;
    top: 146px;
  }
  .website {
    margin: 0;
    font-size: 44px;
    font-weight: 800;
    line-height: 56px;
    letter-spacing: -0.3px;
  }
  .email-list {
    list-style: none;
    margin: 48px 0 0;
    padding: 0;
  }
  .email-list li {
    font-size: 39px;
    font-weight: 300;
    line-height: 50.4px;
    letter-spacing: 0.4px;
  }
</style>
</head>
<body>
  <main class="canvas">
    <section class="card">
      <div class="contact">
        <p class="website">www.tkservicing.com.au</p>
        <ul class="email-list">
          <li>admin@tkservicing.com.au</li>
          <li>sales@tkservicing.com.au</li>
          <li>accounts@tkservicing.com.au</li>
          <li>parts@tkservicing.com.au</li>
          <li>office@tkservicing.com.au</li>
        </ul>
      </div>
    </section>
  </main>
</body>
</html>
```